One Page Website for Personal Trainer in London

I have a logo and need a one page website designed around my branding. I am a freelance Personal Trainer based in London specialising in bodyweight training for men and women. I would like the site to be modern and clean but not overtly urban in design.
I need the following headings:
About Me
My Services
Events
Blog
I don't need them to be seperate pages but if they can link to further down the page that would be great.
Industry/Entity Type
Personal Trainer
Coding
Coded - Design and coding required
Number of Pages Required
1 page
Requirements
Must have
- I need the following headings:
- About Me
- My Services
- Events
- Blog
- mobile friendly formatting
- health and fitness related photography
- Colour scheme in keeping with my existing logo

```html
<!DOCTYPE html>
<html lang="en">
<head>
<meta charset="utf-8">
<title>Marlow Reid – Personal Training</title>
<link href="https://fonts.googleapis.com/css2?family=Open+Sans:ital,wght@0,400;0,600;0,700;0,800;1,400;1,600;1,700&display=swap" rel="stylesheet">
<style>
:root{
  --orange:#f7941d;
  --dark:#2b2b2b;
  --ink:#222;
  --muted:#8a8a8a;
  --light:#f2f2f2;
  --white:#fff;
  --line:#d9d9d9;
}
*{box-sizing:border-box;margin:0;padding:0}
html,body{width:1200px;height:3939px;overflow:hidden}
body{position:relative;font-family:"Open Sans",Arial,sans-serif;color:var(--ink);background:var(--white)}
a{color:inherit;text-decoration:none}
.abs{position:absolute}

/* header */
.top-strip{left:0;top:0;width:1200px;height:10px;background:var(--dark)}
.brand{left:142px;top:44px;display:flex;align-items:center;gap:12px}
.brand-dot{width:34px;height:34px;border-radius:50%;background:var(--orange)}
.brand-name{font-size:26px;font-weight:600;color:var(--dark)}
.contact{top:66px;display:flex;align-items:center;gap:10px;font-size:21px;font-weight:700;color:var(--dark)}
.contact .ico{width:30px;height:30px}
.contact.phone{left:654px}
.contact.mail{left:862px}

.nav{left:0;top:142px;width:1200px;height:34px;background:var(--orange)}
.nav ul{list-style:none;position:absolute;left:137px;top:0;display:flex;height:34px}
.nav li{height:34px;display:flex;align-items:center;justify-content:center;font-size:12.5px;font-weight:700;text-transform:uppercase;color:var(--dark);border-right:1px solid rgba(0,0,0,.15)}
.nav li.active{background:var(--dark);color:var(--orange)}
.nav li.cta{background:var(--dark);color:var(--white);border:none}

/* hero */
.hero{left:0;top:176px;width:1200px;height:680px;background:linear-gradient(100deg,#5d5b59 0%,#9a9896 35%,#c9c8c6 60%,#b9b8b6 100%)}
.hero-copy{right:97px;top:310px;text-align:right;color:var(--dark)}
.hero-copy .lead{font-size:46px;font-style:italic;font-weight:600;line-height:1}
.hero-copy .big{font-size:72px;font-weight:800;line-height:.95;letter-spacing:-1px;text-transform:uppercase;margin-top:8px}
.hero-copy .tail{font-size:28px;font-weight:400;margin-top:4px}

/* about */
.about-title{left:147px;top:955px;font-size:44px;font-weight:700}
.rule{height:4px;width:40px;background:var(--orange)}
.about-rule{left:147px;top:1015px}
.about-sub{left:142px;top:1044px;width:420px;font-size:14.5px;font-weight:700;line-height:1.45;text-transform:uppercase}
.about-body{left:142px;top:1122px;width:420px;font-size:12.5px;color:var(--muted);line-height:1.65}
.btn{display:flex;height:37px}
.btn .label{background:var(--orange);color:var(--white);font-size:11.5px;font-weight:700;text-transform:uppercase;display:flex;align-items:center;padding:0 22px}
.btn .cap{width:37px;background:var(--dark)}
.about-btn{left:142px;top:1250px}
.about-photo{left:633px;top:969px;width:420px;height:318px;background:linear-gradient(135deg,#6d6660,#a99c92 50%,#4b4642)}

/* banner */
.banner{left:0;top:1410px;width:1200px;height:476px;background:linear-gradient(180deg,#7a7470,#a7a19c 50%,#6d6763)}
.banner-copy{left:0;top:1562px;width:1200px;text-align:center;color:var(--white)}
.banner-copy .small{font-size:21px;font-style:italic;font-weight:600}
.banner-copy .big{font-size:56px;font-weight:600;line-height:1.05;margin-top:10px}

/* services */
.section-title{left:0;width:1200px;text-align:center;font-size:44px;font-weight:700}
.center-rule{left:580px}
.services-title{top:1940px}
.services-rule{top:2014px}
.service{width:268px;text-align:center}
.service .shot{height:176px}
.service h3{margin-top:20px;font-size:16px;font-weight:700;color:var(--orange)}
.service p{margin:8px auto 0;width:230px;font-size:11px;line-height:1.45;color:var(--ink)}
.services-btn{left:525px;top:2374px}

/* blog */
.blog{left:0;top:2476px;width:1200px;height:714px;background:var(--orange)}
.blog-title{top:2530px;color:var(--white)}
.blog-rule{top:2612px;background:var(--white)}
.post{top:2663px;width:268px;height:328px;background:var(--white);border-radius:4px;overflow:hidden}
.post .shot{height:189px;position:relative}
.post .date{position:absolute;left:0;top:0;width:50px;height:54px;background:var(--orange);color:var(--white);text-align:center;font-size:26px;font-weight:700;line-height:40px}
.post .date small{display:block;font-size:8px;line-height:6px;font-weight:600}
.post h4{margin:18px 18px 0;font-size:15px;font-weight:700;line-height:1.3}
.post p{margin:10px 18px 0;font-size:11px;line-height:1.45;color:#555}
.blog-btn{left:525px;top:3072px}
.blog-btn .label{background:var(--white);color:var(--dark)}

/* events & testimonials */
.lower{left:0;top:3190px;width:1200px;height:429px;background:var(--light)}
.col-head{top:3252px;font-size:28px;font-weight:600;color:var(--orange)}
.arrows{top:3259px;display:flex;gap:6px}
.arrows span{width:20px;height:20px;border-radius:50%;background:var(--orange);display:flex;align-items:center;justify-content:center}
.col-line{top:3307px;height:2px;background:var(--line)}
.event{left:100px;width:460px;display:flex;gap:28px}
.event .day{width:63px;flex:none;text-align:center}
.event .day b{display:block;height:40px;background:var(--dark);color:var(--white);font-size:24px;line-height:40px}
.event .day i{display:block;height:31px;background:var(--orange);color:var(--white);font-style:normal;font-size:15px;line-height:31px}
.event h5{font-size:15px;font-weight:700;margin-top:8px}
.event p{font-size:12px;color:#555;line-height:1.5;margin-top:8px}
.event-sep{left:100px;top:3430px;width:457px;height:1px;background:var(--line)}
.avatar{left:664px;top:3327px;width:137px;height:137px;border-radius:50%;border:5px solid var(--white);background:radial-gradient(circle at 50% 40%,#d7b7a4,#8e6b5c)}
.client{left:664px;top:3478px;width:137px;text-align:center;font-size:13px;font-weight:700;color:var(--orange);text-transform:uppercase}
.quote{left:830px;top:3335px;width:292px;font-size:12.5px;font-style:italic;line-height:1.55;color:#444}
.quote b{color:var(--orange);font-size:22px;font-style:normal}

/* footer */
.footer{left:0;top:3619px;width:1200px;height:320px;background:var(--dark);text-align:center;color:var(--white)}
.footer .addr{margin-top:75px;font-size:16px;font-weight:700}
.footer .tel{margin-top:4px;font-size:16px;font-weight:700;color:var(--orange)}
.socials{display:flex;justify-content:center;gap:22px;margin-top:48px}
.socials span{width:16px;height:16px;border-radius:50%;background:var(--white)}
.footer .copy{margin-top:42px;font-size:10px;color:#888}
</style>
</head>
<body>

<header>
  <div class="abs top-strip"></div>
  <div class="abs brand"><span class="brand-dot"></span><span class="brand-name">Marlow Reid</span></div>
  <div class="abs contact phone">
    <svg class="ico" viewBox="0 0 30 30"><circle cx="15" cy="15" r="13" fill="none" stroke="#f7941d" stroke-width="3"/><path d="M10 9l3 0 1 4-2 1.5a8 8 0 0 0 3.5 3.5L17 16l4 1v3c-6 1-12-5-11-11z" fill="#f7941d"/></svg>
    (555) 014 2287
  </div>
  <div class="abs contact mail">
    <svg class="ico" viewBox="0 0 30 30"><circle cx="15" cy="15" r="13" fill="none" stroke="#f7941d" stroke-width="3"/><rect x="9" y="11" width="12" height="8" fill="#f7941d"/><path d="M9 11l6 5 6-5" fill="none" stroke="#fff" stroke-width="1.2"/></svg>
    info@marlowreid.co.uk
  </div>
  <nav class="abs nav">
    <ul>
      <li class="active" style="width:104px"><a href="#top">Home</a></li>
      <li style="width:128px"><a href="#about">About Me</a></li>
      <li style="width:148px"><a href="#services">My Services</a></li>
      <li style="width:100px"><a href="#events">Events</a></li>
      <li style="width:96px"><a href="#blog">Blog</a></li>
      <li style="width:161px"><a href="#events">Contact Us</a></li>
      <li class="cta" style="width:203px"><a href="#services">Start Training Now</a></li>
    </ul>
  </nav>
</header>

<section id="top">
  <div class="abs hero" role="img" aria-label="Photo of a woman doing a bodyweight push-up on a gym floor"></div>
  <div class="abs hero-copy">
    <div class="lead">Start adding</div>
    <div class="big">Body Weight<br>Movements</div>
    <div class="tail">into your training &amp; enjoy the results!</div>
  </div>
</section>

<section id="about">
  <h2 class="abs about-title">About us</h2>
  <div class="abs rule about-rule"></div>
  <p class="abs about-sub">Negare non possum. Dolere malum est: in crucem qui agitur, beatus esse non potest. Quae cum dixisset paulumque institisset</p>
  <p class="abs about-body">Every session is built around your body, your goals and your week. We work on strength, balance and mobility with simple movements you can repeat anywhere, at home or in the park.</p>
  <a class="abs btn about-btn" href="#about"><span class="label">Read More</span><span class="cap"></span></a>
  <div class="abs about-photo" role="img" aria-label="Photo of a woman resting between sets in a gym"></div>
</section>

<section>
  <div class="abs banner" role="img" aria-label="Photo of a man and a woman doing squat jumps in a bright studio"></div>
  <div class="abs banner-copy">
    <div class="small">I am a freelance Personal Trainer based in London specialising in</div>
    <div class="big">Bodyweight training for<br>men and women.</div>
  </div>
</section>

<section id="services">
  <h2 class="abs section-title services-title">Our Service</h2>
  <div class="abs rule center-rule services-rule"></div>
  <div class="abs service" style="left:171px;top:2064px">
    <div class="shot" role="img" aria-label="Photo of a woman stretching on a beach" style="background:linear-gradient(180deg,#a9c3dc,#d8e4ee 60%,#bfb6a6)"></div>
    <h3>Stretching</h3>
    <p>Gentle flexibility work to ease tight muscles and aid recovery.</p>
  </div>
  <div class="abs service" style="left:467px;top:2064px">
    <div class="shot" role="img" aria-label="Photo of a man training on a bench" style="background:linear-gradient(135deg,#5f7fa0,#a3b3c2 50%,#c98f63)"></div>
    <h3>Bodyweight Exercise</h3>
    <p>Push, pull and squat patterns using only your own weight.</p>
  </div>
  <div class="abs service" style="left:764px;top:2064px">
    <div class="shot" role="img" aria-label="Photo of fitness gear and a workout plan laid out" style="background:linear-gradient(135deg,#7b7d80,#b04a58 45%,#e0a33b 75%,#6f7b87)"></div>
    <h3>Fitness Plans</h3>
    <p>Clear weekly plans that fit around work and family life.</p>
  </div>
  <a class="abs btn services-btn" href="#services"><span class="label">More Service</span><span class="cap"></span></a>
</section>

<section id="blog">
  <div class="abs blog"></div>
  <h2 class="abs section-title blog-title">Latest Blog</h2>
  <div class="abs rule center-rule blog-rule"></div>

  <article class="abs post" style="left:42px">
    <div class="shot" role="img" aria-label="Photo of a woman catching her breath after a workout" style="background:linear-gradient(135deg,#3e6f8a,#b98c78 55%,#7f5c56)"><div class="date">22<small>October</small></div></div>
    <h4>Negare non possum. Dolere malum est</h4>
    <p>Short circuits you can finish in twenty minutes before work.</p>
  </article>
  <article class="abs post" style="left:325px">
    <div class="shot" role="img" aria-label="Photo of two people jogging outdoors" style="background:linear-gradient(135deg,#d7d2cb,#9c8c7f 50%,#5b5855)"><div class="date">23<small>October</small></div></div>
    <h4>Quod autem satis est, eo quic uid accessit</h4>
    <p>How to keep going when the first month gets hard.</p>
  </article>
  <article class="abs post" style="left:608px">
    <div class="shot" role="img" aria-label="Photo of a woman lifting a light dumbbell" style="background:linear-gradient(135deg,#c9c9c9,#b88c7c 45%,#8e6fb0 75%,#e0e0e0)"><div class="date">24<small>October</small></div></div>
    <h4>Alios in primisque familiarem nostrum Posidonium</h4>
    <p>Simple food habits that support steady training progress.</p>
  </article>
  <article class="abs post" style="left:891px">
    <div class="shot" role="img" aria-label="Photo of running shoes on a sunlit trail" style="background:linear-gradient(135deg,#f2c14a,#d9823a 50%,#6a4a3a)"><div class="date">25<small>October</small></div></div>
    <h4>Vicimus. Hanc ergo intuens debet institutum</h4>
    <p>Why running drills improve your bodyweight strength sessions.</p>
  </article>

  <a class="abs btn blog-btn" href="#blog"><span class="label">View All Blog Posts</span><span class="cap"></span></a>
</section>

<section id="events">
  <div class="abs lower"></div>
  <h3 class="abs col-head" style="left:94px">Events</h3>
  <div class="abs arrows" style="left:514px">
    <span><svg width="8" height="10" viewBox="0 0 8 10"><path d="M6 1L2 5l4 4" fill="none" stroke="#fff" stroke-width="2"/></svg></span>
    <span><svg width="8" height="10" viewBox="0 0 8 10"><path d="M2 1l4 4-4 4" fill="none" stroke="#fff" stroke-width="2"/></svg></span>
  </div>
  <div class="abs col-line" style="left:94px;width:463px"></div>

  <div class="abs event" style="top:3340px">
    <div class="day"><b>30</b><i>Oct</i></div>
    <div><h5>Verum tamen cum de rebus</h5><p>Outdoor group session in the park, all levels welcome to join.</p></div>
  </div>
  <div class="abs event-sep"></div>
  <div class="abs event" style="top:3448px">
    <div class="day"><b>31</b><i>Oct</i></div>
    <div><h5>Verum tamen cum de rebus</h5><p>Beginner workshop on form, breathing and safe progressions.</p></div>
  </div>

  <h3 class="abs col-head" style="left:659px">Testimonials</h3>
  <div class="abs arrows" style="left:1078px">
    <span><svg width="8" height="10" viewBox="0 0 8 10"><path d="M6 1L2 5l4 4" fill="none" stroke="#fff" stroke-width="2"/></svg></span>
    <span><svg width="8" height="10" viewBox="0 0 8 10"><path d="M2 1l4 4-4 4" fill="none" stroke="#fff" stroke-width="2"/></svg></span>
  </div>
  <div class="abs col-line" style="left:659px;width:463px"></div>
  <div class="abs avatar" role="img" aria-label="Portrait photo of a client"></div>
  <div class="abs client">Hannah</div>
  <p class="abs quote"><b>&ldquo;</b> Three months in and I feel stronger than ever. Sessions are friendly, focused and always varied, and I can now train confidently on my own at home. <b>&rdquo;</b></p>
</section>

<footer class="abs footer">
  <div class="addr">42 Kestrel Row, Islington, London N1 4QT</div>
  <div class="tel">Phone (555) 014 2287</div>
  <div class="socials"><span></span><span></span><span></span><span></span></div>
  <div class="copy">© 2017 All rights reserved by Marlow Reid</div>
</footer>

</body>
</html>
```